Personal Injury Book Ad Photo Set

I need a series of images for a Threadloop ad campaign for promoting a book titled "Making Sense of an Accident Claim".

```html
<!DOCTYPE html>
<html lang="en">
<head>
<meta charset="utf-8">
<title>Making Sense of an Accident Claim – Book Ad</title>
<link rel="stylesheet" href="https://fonts.googleapis.com/css2?family=Bebas+Neue&family=Cinzel:wght@400;500&display=swap">
<style>
  :root {
    --page-bg: #ffffff;
    --gold: #a8860a;
    --gold-dark: #7a6006;
    --gold-light: #c49d1c;
    --band-blue: #0a5cf0;
    --book-blue: #0b3fc8;
    --book-edge: #1a4fd8;
    --pages: #e9ecf3;
    --white: #ffffff;
    --headline-shadow: #4a3a05;
    --button-yellow: #ffd21a;
    --button-edge: #e0a800;
    --button-text: #1c1c1c;
    --sky: #cfdbe6;
    --ground: #b9a994;
  }
  html, body {
    margin: 0;
    width: 1200px;
    height: 900px;
    overflow: hidden;
    background: var(--page-bg);
  }
  .banner {
    position: absolute;
    left: 150px;
    top: 214px;
    width: 900px;
    height: 449px;
    overflow: hidden;
    box-shadow: 0 10px 18px rgba(0,0,0,0.35);
  }
  .banner-shapes {
    position: absolute;
    inset: 0;
  }
  .headline {
    position: absolute;
    left: 54px;
    top: 60px;
    margin: 0;
    font-family: "Bebas Neue", "Oswald", sans-serif;
    font-weight: 400;
    color: var(--white);
    line-height: 1;
    text-shadow: 3px 3px 0 var(--headline-shadow);
  }
  .headline span { display: block; }
  .headline .line-small { font-size: 60px; height: 64px; }
  .headline .line-large { font-size: 112px; height: 104px; }
  .headline .line-medium { font-size: 61px; height: 66px; }
  .headline .line-final { font-size: 112px; }
  .buy-button {
    position: absolute;
    left: 307px;
    top: 348px;
    width: 124px;
    height: 35px;
    border-radius: 18px;
    background: linear-gradient(#ffe55c, var(--button-yellow) 55%, var(--button-edge));
    box-shadow: 2px 3px 0 var(--headline-shadow);
    font-family: "Bebas Neue", sans-serif;
    font-size: 27px;
    line-height: 37px;
    text-align: center;
    color: var(--button-text);
  }
  .book-cover-text {
    position: absolute;
    left: 468px;
    top: 48px;
    width: 210px;
    height: 350px;
    font-family: "Cinzel", serif;
    color: var(--white);
    text-align: center;
    transform: skewY(-2deg);
  }
  .book-cover-text span {
    position: absolute;
    left: 0;
    right: 0;
    line-height: 1;
  }
  .cover-l1 { top: 56px; font-size: 19px; }
  .cover-l2 { top: 88px; font-size: 46px; }
  .cover-l3 { top: 142px; font-size: 30px; }
  .cover-l4 { top: 184px; font-size: 30px; }
  .cover-l5 { top: 226px; font-size: 38px; }
  .cover-foot { top: 308px; font-size: 11px; transform: skewY(4deg); }
</style>
</head>
<body>
  <section class="banner">
    <svg class="banner-shapes" width="900" height="449" viewBox="0 0 900 449">
      <defs>
        <linearGradient id="goldFill" x1="0" y1="0" x2="1" y2="1">
          <stop offset="0" stop-color="var(--gold-dark)"/>
          <stop offset="0.5" stop-color="var(--gold-light)"/>
          <stop offset="1" stop-color="var(--gold)"/>
        </linearGradient>
        <linearGradient id="sceneFill" x1="0" y1="0" x2="0" y2="1">
          <stop offset="0" stop-color="var(--sky)"/>
          <stop offset="0.6" stop-color="#d8cbb8"/>
          <stop offset="1" stop-color="var(--ground)"/>
        </linearGradient>
      </defs>
      <rect class="scene-photo" x="400" y="0" width="500" height="449" fill="url(#sceneFill)"
            role="img" aria-label="Photo of a runner sitting on a bridge holding an injured knee"/>
      <polygon class="band" points="444,0 495,0 654,449 603,449" fill="var(--band-blue)"/>
      <polygon class="gold-panel" points="0,0 444,0 603,449 0,449" fill="url(#goldFill)"
               role="img" aria-label="Gold-tinted photo of a judge's gavel and scales of justice"/>
      <polygon class="book-pages" points="677,34 689,40 690,404 678,410" fill="var(--pages)" stroke="var(--book-edge)" stroke-width="1.5"/>
      <polygon class="book-cover" points="468,62 677,34 678,410 466,386" fill="var(--book-blue)"/>
    </svg>

    <h1 class="headline">
      <span class="line-small">Making Sense</span>
      <span class="line-large">Of An</span>
      <span class="line-medium">Accident</span>
      <span class="line-final">Claim</span>
    </h1>
    <div class="buy-button">Buy Now</div>

    <div class="book-cover-text">
      <span class="cover-l1">Making Sense</span>
      <span class="cover-l2">Of An</span>
      <span class="cover-l3">Accident</span>
      <span class="cover-l4">Claim</span>
      <span class="cover-l5">Guide</span>
      <span class="cover-foot">Your Book Cover Here</span>
    </div>
  </section>
</body>
</html>
```